Employee Wellbeing Model Graphic Design

A visual/graphic representation of our Employee Wellbeing model.
Our model is a combination of the Ngā Kiri Rehu Pona model of health and wellbeing and the wellbeing continuum.
We would like the visual to be on one page. The design should be modern and simple.
The powerpoint attached shows the information we are wanting to share with our employees about our wellbeing programme.

Target Market(s)

Our employees

Industry/Entity Type

Event Management

Font styles to use
Sans Serif
Other font styles liked:
• calibri light

Colors
00AB8E
00BBA5
67D7C9
C6EFE9
E9F9F6

```html
<!DOCTYPE html>
<html lang="en">
<head>
<meta charset="utf-8">
<title>Employee Wellbeing Model</title>
<link rel="stylesheet" href="https://fonts.googleapis.com/css2?family=Bebas+Neue&family=Oswald:wght@400;500&display=swap">
<style>
  :root {
    --teal-light: #00BBA5;
    --teal-deep: #00AB8E;
    --white: #ffffff;
    --ink: #1a1a1a;
    --tab-1: #1f7a2e;
    --tab-2: #2a8a44;
    --tab-3: #2e9a58;
    --tab-4: #30a268;
    --tab-land: #1ea0dc;
    --unwell: #e8336a;
    --struggling: #f7a23b;
    --going-ok: #b5c334;
    --thriving: #7cbf5a;
  }
  * { margin: 0; padding: 0; box-sizing: border-box; }
  html, body { width: 1200px; height: 750px; overflow: hidden; background: var(--white); }
  .sheet { position: relative; width: 1200px; height: 750px; background: var(--white); font-family: "Oswald", sans-serif; color: var(--ink); }

  .intro-panel { position: absolute; left: 0; top: 0; width: 272px; height: 413px; background: var(--teal-light); color: var(--white); padding: 30px 20px 0 33px; }
  .intro-title { font-family: "Bebas Neue", sans-serif; font-weight: 400; font-size: 62px; line-height: 76px; letter-spacing: 1px; }
  .intro-text { margin-top: 22px; font-size: 15.5px; line-height: 22.5px; font-weight: 400; }

  .whare-mark { position: absolute; left: 355px; top: 54px; width: 400px; height: 266px; }

  .dimension-list { position: absolute; left: 803px; top: 40px; width: 181px; list-style: none; }
  .dimension { height: 68.5px; }
  .dimension-name { display: block; height: 32px; line-height: 32px; padding-left: 11px; color: var(--white); font-weight: 500; font-size: 18px; border-top-right-radius: 14px; }
  .dimension-meaning { display: block; padding-left: 11px; margin-top: 5px; font-size: 16px; line-height: 22px; }
  .dimension:nth-child(1) .dimension-name { background: var(--tab-1); }
  .dimension:nth-child(2) .dimension-name { background: var(--tab-2); }
  .dimension:nth-child(3) .dimension-name { background: var(--tab-3); }
  .dimension:nth-child(4) .dimension-name { background: var(--tab-4); }
  .dimension:nth-child(5) .dimension-name { background: var(--tab-land); }

  .stage-label { position: absolute; top: 434px; width: 140px; text-align: center; font-weight: 500; font-size: 23px; line-height: 30px; }
  .stage-label.unwell { left: 159px; color: var(--unwell); }
  .stage-label.struggling { left: 330px; color: var(--struggling); }
  .stage-label.going-ok { left: 489px; color: var(--going-ok); }
  .stage-label.thriving { left: 646px; color: var(--thriving); }
  .stage-divider { position: absolute; top: 433px; height: 32px; border-left: 1.5px dashed; }
  .stage-divider.d1 { left: 317px; border-color: var(--unwell); }
  .stage-divider.d2 { left: 480px; border-color: var(--struggling); }
  .stage-divider.d3 { left: 644px; border-color: var(--going-ok); }

  .continuum-bar { position: absolute; left: 134px; top: 470px; width: 680px; height: 23px; border-radius: 12px;
    background: linear-gradient(90deg, #e8196a 0%, #f2666a 25%, #f89a3c 42%, #ffd000 50%, #a9c64a 72%, #4cb56f 100%); }

  .stage-notes { position: absolute; top: 501px; list-style: none; font-size: 10.3px; line-height: 13.5px; font-weight: 400; }
  .stage-notes li { position: relative; padding-left: 5px; margin-bottom: 13.5px; }
  .stage-notes li::before { content: "·"; position: absolute; left: -2px; font-weight: 500; }
  .stage-notes.unwell { left: 166px; width: 140px; }
  .stage-notes.struggling { left: 335px; width: 130px; }
  .stage-notes.going-ok { left: 496px; width: 138px; }
  .stage-notes.thriving { left: 660px; width: 145px; line-height: 14.7px; }

  .continuum-panel { position: absolute; left: 927px; top: 413px; width: 273px; height: 337px; background: var(--teal-deep); color: var(--white); padding: 20px 16px 0 23px; }
  .continuum-title { font-family: "Bebas Neue", sans-serif; font-weight: 400; font-size: 44px; line-height: 49px; letter-spacing: 1px; }
  .continuum-text { margin-top: 15px; font-size: 15.5px; line-height: 21px; }
</style>
</head>
<body>
<main class="sheet">
  <section class="intro-panel">
    <h1 class="intro-title">Ngā Kiri<br>Rehu Pona</h1>
    <p class="intro-text">When all these things are in balance, we thrive. When one or more of these is out of balance our wellbeing is impacted. By aligning workplace activities with Ngā Kiri Rehu Pona, organizations can create an environment where well-being is valued, and employees thrive</p>
  </section>

  <svg class="whare-mark" role="img" aria-label="Meeting house symbol representing the four walls of wellbeing" viewBox="0 0 400 266">
    <defs>
      <linearGradient id="whare-fill" x1="0" y1="1" x2="1" y2="0">
        <stop offset="0" stop-color="#0f5e63"/>
        <stop offset="1" stop-color="#8cbf26"/>
      </linearGradient>
    </defs>
    <rect width="400" height="266" rx="10" fill="url(#whare-fill)" opacity="0.85"/>
  </svg>

  <ul class="dimension-list">
    <li class="dimension"><span class="dimension-name">Taha Hinegaro</span><span class="dimension-meaning">Mental/Emotional</span></li>
    <li class="dimension"><span class="dimension-name">Tana Tinana</span><span class="dimension-meaning">Physical Health</span></li>
    <li class="dimension"><span class="dimension-name">Taha Whanau</span><span class="dimension-meaning">Family/Community</span></li>
    <li class="dimension"><span class="dimension-name">Taha Wairua</span><span class="dimension-meaning">Spiritual Health</span></li>
    <li class="dimension"><span class="dimension-name">Whenua</span><span class="dimension-meaning">Land/Roots</span></li>
  </ul>

  <span class="stage-label unwell">Unwell</span>
  <span class="stage-label struggling">Struggling</span>
  <span class="stage-label going-ok">Going OK</span>
  <span class="stage-label thriving">Thriving</span>
  <span class="stage-divider d1"></span>
  <span class="stage-divider d2"></span>
  <span class="stage-divider d3"></span>
  <div class="continuum-bar"></div>

  <ul class="stage-notes unwell">
    <li>People who are mentally unwell and/or have a diagnosed mental illness</li>
    <li>Severe and persistent functional impairment</li>
    <li>Neurochemical process outside of the individuals' control is often</li>
  </ul>
  <ul class="stage-notes struggling">
    <li>People who don't meet the criteria for a diagnosable mental illness, but who may be highly stressed or distressed</li>
    <li>More severe and persistent functional impairment</li>
    <li>A mental health problem develops</li>
    <li>Usual coping mechanisms may not suffice or don't have the same impact</li>
  </ul>
  <ul class="stage-notes going-ok">
    <li>People who lack general mental wellbeing and a sense of being reasonably happy with life</li>
    <li>Often show as disengaged and unmotivated, lack meaning and purpose in their daily lives</li>
    <li>Likely to have higher rates of physical illness and workplace accidents</li>
    <li>People develop coping mechanisms which can be applied to help revert to full mental health – thriving</li>
  </ul>
  <ul class="stage-notes thriving">
    <li>People who are experiencing optimal/positive mental health.</li>
    <li>Engaged, generally happy, getting enough good quality sleep and eating well, experiencing positive relationships, and have a strong sense of meaning and purpose in life</li>
    <li>Likely to experience better physical health and higher productivity</li>
  </ul>

  <section class="continuum-panel">
    <h2 class="continuum-title">The<br>Wellbeing<br>Continuum</h2>
    <p class="continuum-text">People can have a range of mental health experiences across the continuum that will change over time. It is usual to cycle across the Thriving and Going OK parts of the spectrum</p>
  </section>
</main>
</body>
</html>
```